Brindle Grass Services website design

We want to create a Sports turf website for our business Brindle Grass Services - we do sports turf management on sports fields around the Mackay region soccer rugby league softball fields etc from full turf management plans and maintenance to just supply and apply of turf management products and just supply of products with program we also do grounds facility maintenance at council facility's and grounds that require a higher level of care - we will up load our logos and fonts etc to assist with the colour pallet for the website - we will have to have a landing page a shop page with tabs a gallery tab along with a grants initiative and our coastals finest green tab also - our font for the txt is called ethnocentric
Updates

how do we open time for people to submit we have no one submitted

Industry/Entity Type

Turf

Coding

Coded - Design and coding required

Number of Pages Required

5+ page

Font styles to use
Other font styles liked:
• ethnocentric

Requirements
Must have
• I have mentioned some waffle in the description that should assist
Should not have
• anything not related

```html
<!DOCTYPE html>
<html lang="en">
<head>
<meta charset="utf-8">
<title>Brindle Grass Services</title>
<link href="https://fonts.googleapis.com/css2?family=Inter:wght@400;500;600;700;800&family=Orbitron:wght@900&display=swap" rel="stylesheet">
<style>
:root{
  --green:#2e7d32;
  --green-dark:#1b5e20;
  --green-mid:#43a047;
  --green-soft:#e8f3e6;
  --gray-bg:#f5f7f9;
  --text:#333;
  --muted:#6b6b6b;
  --dark:#262a2e;
  --white:#fff;
  --star:#f5c518;
}
*{box-sizing:border-box;margin:0;padding:0}
html,body{width:1200px;height:4706px;overflow:hidden}
body{font-family:'Inter',sans-serif;color:var(--text);background:var(--white)}
.wrap{width:1080px;margin:0 auto;position:relative}
.section-title{text-align:center;color:var(--green-dark);font-size:34px;font-weight:700}
.title-bar{width:52px;height:3px;background:var(--green);margin:10px auto 12px}
.section-sub{text-align:center;color:var(--muted);font-size:14px}

/* header */
.site-header{height:77px;background:#fff;box-shadow:0 2px 6px rgba(0,0,0,.08);position:relative;z-index:2}
.site-header .wrap{display:flex;align-items:center;justify-content:space-between;height:77px}
.logo{display:flex;align-items:center;gap:10px;font-weight:800;font-size:21px;color:var(--green-dark)}
.logo-mark{width:18px;height:18px;background:var(--green)}
.nav{display:flex;gap:20px;font-size:15px;font-weight:500;color:var(--green)}

/* hero */
.hero{height:663px;position:relative;color:#fff;text-align:center;overflow:hidden}
.hero-bg{position:absolute;inset:0;background:radial-gradient(ellipse at 55% 45%,#3f7a38 0%,#2f6a2c 45%,#22561f 100%)}
.hero-inner{position:relative;padding-top:70px}
.hero h1{font-family:'Orbitron',sans-serif;font-weight:900;font-size:58px;line-height:72px;letter-spacing:2px}
.hero-sub{font-size:22px;margin-top:26px}
.tags{display:flex;flex-wrap:wrap;justify-content:center;gap:10px;width:560px;margin:48px auto 0}
.tag{background:#5fb04c;border-radius:8px;padding:7px 16px;font-size:14px;font-weight:600;display:flex;align-items:center;gap:6px}
.tag i{width:10px;height:10px;border-radius:50%;background:#fff;display:inline-block}
.hero-btns{display:flex;justify-content:center;gap:22px;margin-top:60px}
.btn-solid,.btn-ghost{width:182px;height:63px;border-radius:6px;font-size:18px;font-weight:700;display:flex;align-items:center;justify-content:center}
.btn-solid{background:var(--green-mid)}
.btn-ghost{border:2px solid #fff}

/* services */
.services{height:785px;padding-top:78px}
.service-grid{display:grid;grid-template-columns:repeat(3,345px);gap:20px 22px;margin-top:60px}
.service-card{background:#fff;border-top:3px solid var(--green);border-radius:6px;box-shadow:0 3px 10px rgba(0,0,0,.1);text-align:center;padding:28px 32px 0;height:268px}
.service-grid .row2{height:241px}
.icon-circle{width:68px;height:68px;border-radius:50%;background:var(--green);margin:0 auto;display:flex;align-items:center;justify-content:center}
.service-card h3{color:var(--green-dark);font-size:20px;font-weight:700;margin:24px 0 18px;line-height:25px}
.service-card p{font-size:13px;color:var(--muted);line-height:21px}

/* shop */
.shop{height:593px;background:var(--gray-bg);padding-top:40px}
.product-grid{display:grid;grid-template-columns:repeat(4,255px);gap:20px;margin-top:72px}
.product-card{background:#fff;border-radius:8px;box-shadow:0 3px 10px rgba(0,0,0,.08);height:307px;text-align:center;padding-top:27px}
.product-icon{width:82px;height:82px;border-radius:8px;background:linear-gradient(160deg,#e3f2de,#a8d59c);margin:0 auto;display:flex;align-items:center;justify-content:center}
.product-card h3{font-size:17px;font-weight:700;color:var(--green-dark);margin:26px 0 8px}
.product-card p{font-size:12px;color:var(--muted);line-height:20px;padding:0 22px;height:40px}
.price{font-size:19px;font-weight:700;color:var(--green-dark);margin:12px 0 16px}
.cart-btn{display:inline-block;background:var(--green);color:#fff;font-size:11px;font-weight:600;padding:8px 20px;border-radius:4px}
.view-all{display:block;width:158px;margin:22px auto 0;border:2px solid var(--green);border-radius:5px;color:var(--green);text-align:center;font-size:13px;font-weight:600;padding:8px 0}

/* about */
.about{height:497px;padding-top:39px}
.about .wrap{display:flex;gap:40px}
.about-text{width:530px}
.about-text h2{font-size:33px;font-weight:700;color:var(--green-dark)}
.about-lead{font-size:16px;color:var(--muted);line-height:26px;margin:14px 0 16px}
.about-text p.body{font-size:13px;line-height:21px;margin-bottom:16px}
.stats{display:flex;justify-content:space-between;padding:0 4px;margin-top:30px}
.stat{text-align:center;width:160px}
.stat b{display:block;font-size:34px;color:var(--green);font-weight:700}
.stat span{font-size:11px;letter-spacing:1px;color:var(--muted)}
.about-panel{width:530px;height:418px;border-radius:6px;position:relative;overflow:hidden;text-align:center;padding:48px 36px 0}
.about-panel-bg{position:absolute;inset:0;background:linear-gradient(180deg,#dcebd7,#cfe3c9 60%,#dbe9d6)}
.about-panel>*:not(.about-panel-bg){position:relative}
.about-panel h3{font-size:26px;font-weight:700;color:var(--green-dark)}
.about-panel .title-bar{margin:10px auto 16px}
.about-panel p{font-size:14px;line-height:24px;color:#3f4a3e}
.checks{list-style:none;margin-top:18px;font-size:14px;color:var(--green-dark)}
.checks li{display:flex;align-items:center;justify-content:center;gap:10px;margin-bottom:20px}

/* gallery */
.gallery{height:654px;background:var(--green-soft);padding-top:40px}
.gallery-grid{display:grid;grid-template-columns:repeat(3,351px);gap:14px 13px;margin-top:62px}
.tile{height:207px;border-radius:4px;position:relative;display:flex;flex-direction:column;align-items:center;justify-content:center;color:#4caf50;text-align:center}
.tile h4{font-size:20px;font-weight:600;margin-top:56px}
.tile span{font-size:13px;margin-top:8px}
.t1{background:linear-gradient(180deg,#1f3553,#3e6b3a)}
.t2{background:linear-gradient(180deg,#6d6a60,#5a5c48)}
.t3{background:linear-gradient(180deg,#6f7f73,#2b4f7a)}
.t4{background:linear-gradient(180deg,#1a4a8a,#5b77c2)}
.t5{background:linear-gradient(180deg,#4a3d2c,#6a5236)}
.t6{background:linear-gradient(180deg,#2d4a23,#4a3d2a)}

/* reviews */
.reviews{height:502px;padding-top:42px}
.review-grid{display:grid;grid-template-columns:repeat(4,255px);gap:20px;margin-top:74px}
.review{height:279px;background:#fff;border-left:4px solid var(--green);border-radius:6px;box-shadow:0 3px 10px rgba(0,0,0,.08);padding:24px 26px 0 26px}
.stars{color:var(--star);font-size:18px;letter-spacing:4px}
.review q{display:block;font-style:italic;font-size:13px;line-height:21px;margin:14px 0 18px;quotes:none;height:110px}
.review b{display:block;color:var(--green-dark);font-size:13px}
.review small{display:block;color:var(--muted);font-size:12px;margin-top:8px}

/* contact */
.contact{height:517px;background:var(--dark);color:#fff;padding-top:55px}
.contact .section-title{color:#fff}
.contact .section-sub{color:#9aa0a4}
.contact-grid{display:flex;justify-content:space-between;margin-top:70px}
.contact-info{width:500px}
.contact-info h3{color:var(--green);font-size:20px;font-weight:600}
.contact-info>p{font-size:13px;line-height:21px;margin:12px 0 20px}
.info-row{display:flex;gap:18px;margin-bottom:22px;font-size:13px}
.info-row b{display:block;margin-bottom:4px}
.info-row span{color:#66bb6a}
.form{width:530px}
.form-row{display:flex;gap:16px}
.field{height:47px;border:1px solid #5a6066;border-radius:4px;background:#363b40;color:#66bb6a;font-size:13px;padding:14px;margin-bottom:15px;flex:1}
.field.msg{height:107px}
.send{display:inline-block;background:var(--green);color:#fff;font-size:13px;font-weight:600;padding:9px 20px;border-radius:4px}

/* footer */
.site-footer{height:418px;background:linear-gradient(180deg,#1d5320,#2b7a2e);color:#fff;padding-top:38px}
.footer-cols{display:flex}
.footer-col{font-size:13px}
.footer-col h4{font-size:15px;font-weight:700;margin-bottom:22px}
.footer-col li{list-style:none;margin-bottom:15px}
.f1{width:366px}.f2{width:183px}.f3{width:275px}
.f1 .logo{color:#fff;margin-bottom:22px}
.f1 .logo-mark{background:#fff}
.f1 p{line-height:22px;width:340px}
.socials{display:flex;gap:12px;margin-top:24px}
.socials i{width:30px;height:30px;border-radius:50%;background:rgba(255,255,255,.18);display:block}
.f4 li{display:flex;gap:10px;align-items:flex-start}
.footer-bottom{margin-top:48px;height:58px;background:rgba(0,0,0,.15);display:flex;align-items:center;justify-content:space-between;padding:0 14px;font-size:11px}
.pay{display:flex;gap:8px}
.pay i{width:26px;height:18px;border-radius:3px;background:rgba(255,255,255,.75);display:block}
</style>
</head>
<body>

<header class="site-header">
  <div class="wrap">
    <div class="logo"><span class="logo-mark"></span>Brindle Grass Services</div>
    <nav class="nav"><span>Home</span><span>About</span><span>Services</span><span>Shop</span><span>Gallery</span><span>Reviews</span><span>Contact</span></nav>
  </div>
</header>

<section class="hero">
  <div class="hero-bg" role="img" aria-label="Soccer ball resting on a green sports field"></div>
  <div class="hero-inner">
    <h1>BRINDLE GRASS<br>SERVICES</h1>
    <p class="hero-sub">Premium Sports Turf Solutions for Mackay Region</p>
    <div class="tags">
      <span class="tag"><i></i>Soccer Fields</span>
      <span class="tag"><i></i>Rugby Fields</span>
      <span class="tag"><i></i>Softball Fields</span>
      <span class="tag"><i></i>Facility Maintenance</span>
    </div>
    <div class="hero-btns"><span class="btn-solid">Our Services</span><span class="btn-ghost">Get Quote</span></div>
  </div>
</section>

<section class="services">
  <div class="wrap">
    <h2 class="section-title">Our Services</h2>
    <div class="title-bar"></div>
    <p class="section-sub">Comprehensive turf management solutions for sports facilities</p>
    <div class="service-grid">
      <div class="service-card">
        <div class="icon-circle"><svg width="26" height="26" viewBox="0 0 24 24" fill="#fff"><rect x="5" y="4" width="14" height="18" rx="2"/><rect x="8" y="9" width="8" height="1.6" fill="#2e7d32"/><rect x="8" y="13" width="8" height="1.6" fill="#2e7d32"/><rect x="9" y="2" width="6" height="4" rx="1"/></svg></div>
        <h3>Complete Turf Management Plans</h3>
        <p>Comprehensive turf management strategies tailored to your specific field requirements and usage patterns.</p>
      </div>
      <div class="service-card">
        <div class="icon-circle"><svg width="26" height="26" viewBox="0 0 24 24" stroke="#fff" stroke-width="2.6" stroke-linecap="round"><path d="M5 5l14 14M19 5L5 19"/></svg></div>
        <h3>Maintenance &amp; Care</h3>
        <p>Regular maintenance programs including mowing, fertilization, pest control, and irrigation management.</p>
      </div>
      <div class="service-card">
        <div class="icon-circle"><svg width="26" height="26" viewBox="0 0 24 24" fill="#fff"><path d="M20 4C9 4 4 9 5 18c9 1 15-4 15-14z"/></svg></div>
        <h3>Product Supply &amp; Application</h3>
        <p>High-quality turf management products with professional application services for optimal results.</p>
      </div>
      <div class="service-card row2">
        <div class="icon-circle"><svg width="24" height="26" viewBox="0 0 20 24" fill="#fff"><rect x="2" y="1" width="16" height="22" rx="1"/><g fill="#2e7d32"><rect x="5" y="5" width="3" height="3"/><rect x="12" y="5" width="3" height="3"/><rect x="5" y="11" width="3" height="3"/><rect x="12" y="11" width="3" height="3"/><rect x="8" y="17" width="4" height="6"/></g></svg></div>
        <h3>Grounds Facility Maintenance</h3>
        <p>Specialized maintenance for council facilities requiring higher levels of care and presentation.</p>
      </div>
      <div class="service-card row2">
        <div class="icon-circle"><svg width="26" height="26" viewBox="0 0 24 24" fill="none" stroke="#fff" stroke-width="2.2"><path d="M3 3v18h18"/><path d="M7 15l4-4 3 3 6-6"/></svg></div>
        <h3>Turf Health Programs</h3>
        <p>Customized programs to maintain and improve turf health throughout the seasons.</p>
      </div>
      <div class="service-card row2">
        <div class="icon-circle"><svg width="28" height="24" viewBox="0 0 28 24" fill="#fff"><rect x="1" y="6" width="5" height="10"/><rect x="22" y="6" width="5" height="10"/><path d="M6 7h6l4 3 4-3h2v9l-6 5-10-5z"/></svg></div>
        <h3>Consultation Services</h3>
        <p>Expert advice and recommendations for turf management best practices and problem-solving.</p>
      </div>
    </div>
  </div>
</section>

<section class="shop">
  <div class="wrap">
    <h2 class="section-title">Shop Our Products</h2>
    <div class="title-bar"></div>
    <p class="section-sub">Professional turf management products for your field</p>
    <div class="product-grid">
      <div class="product-card">
        <div class="product-icon"><svg width="32" height="32" viewBox="0 0 24 24" fill="#2e7d32"><path d="M11 22V12C11 6 6 4 3 4c0 5 3 8 8 8zM13 22v-8c0-5 4-7 8-7 0 5-3 7-8 7z"/></svg></div>
        <h3>Premium Grass Seed</h3>
        <p>High-quality grass seed blends for sports fields</p>
        <div class="price">$45.00</div>
        <span class="cart-btn">Add to Cart</span>
      </div>
      <div class="product-card">
        <div class="product-icon"><svg width="30" height="32" viewBox="0 0 24 26" fill="#2e7d32"><rect x="8" y="1" width="8" height="2"/><path d="M9 3h6v7l7 13H2L9 10z"/></svg></div>
        <h3>Turf Fertilizer</h3>
        <p>Professional-grade fertilizers for healthy turf growth</p>
        <div class="price">$65.00</div>
        <span class="cart-btn">Add to Cart</span>
      </div>
      <div class="product-card">
        <div class="product-icon"><svg width="32" height="32" viewBox="0 0 24 24" fill="#2e7d32" stroke="#2e7d32" stroke-width="2" stroke-linecap="round"><ellipse cx="12" cy="14" rx="5" ry="7"/><circle cx="12" cy="6" r="3"/><path d="M3 10h4M17 10h4M3 15h4M17 15h4M4 20l3-2M20 20l-3-2"/></svg></div>
        <h3>Pest Control</h3>
        <p>Safe and effective pest management solutions</p>
        <div class="price">$35.00</div>
        <span class="cart-btn">Add to Cart</span>
      </div>
      <div class="product-card">
        <div class="product-icon"><svg width="26" height="32" viewBox="0 0 20 26" fill="#2e7d32"><path d="M10 1C7 7 2 12 2 17a8 8 0 0016 0c0-5-5-10-8-16z"/></svg></div>
        <h3>Irrigation Solutions</h3>
        <p>Efficient irrigation systems and components</p>
        <div class="price">$125.00</div>
        <span class="cart-btn">Add to Cart</span>
      </div>
    </div>
    <span class="view-all">View All Products</span>
  </div>
</section>

<section class="about">
  <div class="wrap">
    <div class="about-text">
      <h2>About Brindle Grass Services</h2>
      <p class="about-lead">Your trusted partner for premium sports turf management in the Mackay region.</p>
      <p class="body">With years of experience in the industry, we specialize in providing comprehensive turf management solutions for sports fields including soccer, rugby league, and softball fields. Our commitment to excellence and attention to detail ensures that every field we maintain meets the highest standards.</p>
      <p class="body">From complete turf management plans to specialized product supply and application, we offer tailored solutions to meet your specific needs. We also provide grounds facility maintenance for council facilities that require exceptional care and presentation.</p>
      <div class="stats">
        <div class="stat"><b>500+</b><span>FIELDS MAINTAINED</span></div>
        <div class="stat"><b>15+</b><span>YEARS EXPERIENCE</span></div>
        <div class="stat"><b>98%</b><span>CLIENT SATISFACTION</span></div>
      </div>
    </div>
    <div class="about-panel">
      <div class="about-panel-bg" role="img" aria-label="Faded view of a sports stadium and field"></div>
      <h3>Professional Turf Management</h3>
      <div class="title-bar"></div>
      <p>Since 2009, we've been the trusted choice for sports facilities across Mackay and surrounding regions. Our team of certified turf specialists combines cutting-edge techniques with years of hands-on experience.</p>
      <ul class="checks">
        <li><svg width="16" height="16" viewBox="0 0 16 16"><circle cx="8" cy="8" r="8" fill="#43a047"/><path d="M4.5 8.2l2.3 2.3 4.7-4.7" stroke="#fff" stroke-width="1.8" fill="none"/></svg>Certified turf management specialists</li>
        <li><svg width="16" height="16" viewBox="0 0 16 16"><circle cx="8" cy="8" r="8" fill="#43a047"/><path d="M4.5 8.2l2.3 2.3 4.7-4.7" stroke="#fff" stroke-width="1.8" fill="none"/></svg>Environmentally responsible practices</li>
        <li><svg width="16" height="16" viewBox="0 0 16 16"><circle cx="8" cy="8" r="8" fill="#43a047"/><path d="M4.5 8.2l2.3 2.3 4.7-4.7" stroke="#fff" stroke-width="1.8" fill="none"/></svg>Customized maintenance programs</li>
        <li><svg width="16" height="16" viewBox="0 0 16 16"><circle cx="8" cy="8" r="8" fill="#43a047"/><path d="M4.5 8.2l2.3 2.3 4.7-4.7" stroke="#fff" stroke-width="1.8" fill="none"/></svg>24/7 emergency service available</li>
      </ul>
    </div>
  </div>
</section>

<section class="gallery">
  <div class="wrap">
    <h2 class="section-title">Our Work Gallery</h2>
    <div class="title-bar"></div>
    <p class="section-sub">See the quality of our turf management work</p>
    <div class="gallery-grid">
      <div class="tile t1" role="img" aria-label="Floodlit soccer stadium pitch"><h4>Soccer Field</h4><span>Professional maintenance for optimal play</span></div>
      <div class="tile t2" role="img" aria-label="Ball on a rugby field"><h4>Rugby Field</h4><span>Durable turf for high-impact sports</span></div>
      <div class="tile t3" role="img" aria-label="Softball field with balls on the surface"><h4>Softball Field</h4><span>Perfectly maintained diamonds</span></div>
      <div class="tile t4" role="img" aria-label="Turf treatment under a blue sky"><h4>Turf Treatment</h4><span>Advanced care solutions</span></div>
      <div class="tile t5" role="img" aria-label="Hands planting new turf in soil"><h4>New Turf Installation</h4><span>Fresh, vibrant playing surfaces</span></div>
      <div class="tile t6" role="img" aria-label="Hands holding soil with a young plant"><h4>Facility Maintenance</h4><span>Complete grounds care services</span></div>
    </div>
  </div>
</section>

<section class="reviews">
  <div class="wrap">
    <h2 class="section-title">Customer Reviews</h2>
    <div class="title-bar"></div>
    <p class="section-sub">What our clients say about our services</p>
    <div class="review-grid">
      <div class="review"><div class="stars">★★★★★</div><q>"Brindle Grass Services transformed our soccer field. The quality of work and attention to detail is exceptional. Highly recommend!"</q><b>Dean Carver</b><small>Pioneer Soccer Club</small></div>
      <div class="review"><div class="stars">★★★★★</div><q>"Professional service with great results. Our rugby field has never looked better. The team is knowledgeable and reliable."</q><b>Tessa Morland</b><small>Coastal Rugby League</small></div>
      <div class="review"><div class="stars">★★★★★</div><q>"Outstanding maintenance services for our council facilities. Always reliable and the results speak for themselves."</q><b>Grant Ellery</b><small>Coastal Regional Council</small></div>
      <div class="review"><div class="stars">★★★★★</div><q>"The team at Brindle Grass delivered exceptional results for our softball complex. Their expertise and professionalism are unmatched."</q><b>Nina Holt</b><small>Coastal Softball Association</small></div>
    </div>
  </div>
</section>

<section class="contact">
  <div class="wrap">
    <h2 class="section-title">Contact Us</h2>
    <div class="title-bar"></div>
    <p class="section-sub">Get in touch for a free consultation</p>
    <div class="contact-grid">
      <div class="contact-info">
        <h3>Get in Touch</h3>
        <p>Ready to transform your sports field or need expert turf management advice?<br>Contact us today!</p>
        <div class="info-row"><svg width="20" height="20" viewBox="0 0 24 24" fill="#43a047"><path d="M6.6 10.8a15 15 0 006.6 6.6l2.2-2.2c.3-.3.7-.4 1-.2 1.1.4 2.3.6 3.6.6.6 0 1 .4 1 1V20c0 .6-.4 1-1 1A17 17 0 013 4c0-.6.4-1 1-1h3.5c.6 0 1 .4 1 1 0 1.3.2 2.5.6 3.6.1.3 0 .7-.2 1z"/></svg><div><b>Phone</b><span>(07) 4000 XXXX</span></div></div>
        <div class="info-row"><svg width="20" height="20" viewBox="0 0 24 24" fill="#43a047"><path d="M2 5h20v14H2z"/><path d="M2 5l10 8 10-8" stroke="#262a2e" stroke-width="2" fill="none"/></svg><div><b>Email</b><span>info@brindlegrass.com.au</span></div></div>
        <div class="info-row"><svg width="20" height="20" viewBox="0 0 24 24" fill="#43a047"><path d="M12 2a7 7 0 00-7 7c0 5 7 13 7 13s7-8 7-13a7 7 0 00-7-7z"/><circle cx="12" cy="9" r="2.5" fill="#262a2e"/></svg><div><b>Service Area</b><span>Mackay Region, Queensland</span></div></div>
      </div>
      <div class="form">
        <div class="form-row"><div class="field">Your Name</div><div class="field">Your Email</div></div>
        <div class="field" style="display:block">Subject</div>
        <div class="field msg" style="display:block">Your Message</div>
        <span class="send">Send Message</span>
      </div>
    </div>
  </div>
</section>

<footer class="site-footer">
  <div class="wrap">
    <div class="footer-cols">
      <div class="footer-col f1">
        <div class="logo"><span class="logo-mark"></span>Brindle Grass Services</div>
        <p>Premium sports turf management services in the Mackay region. Specializing in soccer, rugby league, and softball field maintenance.</p>
        <div class="socials"><i></i><i></i><i></i><i></i></div>
      </div>
      <div class="footer-col f2"><h4>Quick Links</h4><ul><li>Home</li><li>About Us</li><li>Services</li><li>Shop</li><li>Gallery</li><li>Contact</li></ul></div>
      <div class="footer-col f3"><h4>Services</h4><ul><li>Turf Management Plans</li><li>Maintenance &amp; Care</li><li>Product Supply</li><li>Facility Maintenance</li><li>Turf Health Programs</li><li>Consultation Services</li></ul></div>
      <div class="footer-col f4"><h4>Contact Info</h4><ul>
        <li><svg width="12" height="14" viewBox="0 0 24 24" fill="#a5d6a7"><path d="M12 2a7 7 0 00-7 7c0 5 7 13 7 13s7-8 7-13a7 7 0 00-7-7z"/></svg>Mackay Region, Queensland,<br>Australia</li>
        <li><svg width="12" height="14" viewBox="0 0 24 24" fill="#a5d6a7"><path d="M6.6 10.8a15 15 0 006.6 6.6l2.2-2.2c.3-.3.7-.4 1-.2 1.1.4 2.3.6 3.6.6.6 0 1 .4 1 1V20c0 .6-.4 1-1 1A17 17 0 013 4c0-.6.4-1 1-1h3.5c.6 0 1 .4 1 1 0 1.3.2 2.5.6 3.6z"/></svg>(07) 4000 XXXX</li>
        <li><svg width="12" height="14" viewBox="0 0 24 24" fill="#a5d6a7"><path d="M2 5h20v14H2z"/></svg>info@brindlegrass.com.au</li>
        <li><svg width="12" height="14" viewBox="0 0 24 24" fill="none" stroke="#a5d6a7" stroke-width="3"><circle cx="12" cy="12" r="9"/><path d="M12 7v5l3 2"/></svg>Mon - Fri: 8:00 AM - 5:00 PM</li>
      </ul></div>
    </div>
    <div class="footer-bottom"><span>© 2024 Brindle Grass Services. All rights reserved.</span><div class="pay"><i></i><i></i><i></i><i></i></div></div>
  </div>
</footer>

</body>
</html>
```